EdTech startup needs web (& logo?) redesign

LecternHop.com is a collection of fun online tools designed to help instructors in higher education (i.e. university) build a sense of community in the classroom and enable "active learning." We have spent most of our energy on developing functionality and would love to have some real designers contribute their ideas. Everything (logos, color scheme, images, etc.) is up for grabs, but the winning design should be bootstrap friendly. We are currently using the "Megaframe" template, but are open to others. That being said, we are less interested in getting great code than a great design. Websites we admire include voteswirl.com, workmesh.com, and http://skins.fetchframe.com/products/application

Pages we are particularly interested in ideas for include: homepage, shuffle pick, the grabber, and extra tambourine. The latter three currently use images that probably can't go mainstream.

If you want to participate in the contest we would love for you to check out the site first. In order to enable this, we have set up a fictional class (LPHX 207-3 - Beta Website Redesign). Once you create an account at www.lecternhop.com, you just enter the super-secret invite code "e9a27b41" to add yourself to the class.

Attached our some files that were used to inspire our current design. Feel free to use or ignore them as you see fit. Thanks!

Target Market(s)

college students and their instructors

Industry/Entity Type

Education

Coding

Coded - Design and coding required

Number of Pages Required

4 page

Colors
0355a3
33a6d7
cee9f5

Requirements
Must have
• cool, fun design that is boostrap friendly.
Nice to have
• I like blue, but an open to other color themes.
Should not have
• ?

```html
<!DOCTYPE html>
<html lang="en">
<head>
<meta charset="utf-8">
<title>Lectern Hop</title>
<link href="https://fonts.googleapis.com/css2?family=Kumbh+Sans:wght@500;600;700&family=Roboto:wght@300;400&display=swap" rel="stylesheet">
<style>
:root{
  --navy:#0355a3;
  --sky:#33a6d7;
  --ice:#cee9f5;
  --page:#f3f3f3;
  --card:#ffffff;
  --ink:#444a50;
  --white:#ffffff;
}
*{box-sizing:border-box;margin:0;padding:0}
html,body{width:962px;height:1200px;overflow:hidden}
body{background:var(--page);font-family:"Roboto",sans-serif;color:var(--ink);position:relative}
.hero{position:absolute;left:0;top:0;width:962px;height:492px;
  background:radial-gradient(ellipse at 50% 65%,#9a6f4c 0%,#7a5538 45%,#4d3a2e 100%)}
.hero-photo{position:absolute;inset:0}
.hero-shade{position:absolute;inset:0;background:rgba(20,30,45,.28)}
.topbar{position:absolute;left:48px;right:48px;top:24px;height:32px;display:flex;align-items:center;font-family:"Kumbh Sans",sans-serif}
.brand{display:flex;align-items:center;gap:7px;color:var(--white);font-weight:700;font-size:29px;letter-spacing:-.3px}
.brand-dot{width:30px;height:30px;border-radius:50%;background:var(--sky)}
.nav{display:flex;gap:24px;margin-left:54px;font-size:13.5px;font-weight:600;color:var(--white)}
.nav a{color:inherit;text-decoration:none;padding-bottom:6px}
.nav a.active{color:var(--sky);border-bottom:2px solid var(--sky);padding:0 10px 6px}
.auth{margin-left:auto;display:flex;gap:10px}
.btn-ghost,.btn-solid{font-size:12.5px;font-weight:600;color:var(--white);height:30px;display:flex;align-items:center;justify-content:center;border-radius:2px}
.btn-ghost{width:72px;border:1.5px solid var(--white)}
.btn-solid{width:72px;background:var(--sky);box-shadow:0 2px 0 #1e7fae}
.hero-title{position:absolute;top:175px;left:0;width:962px;text-align:center;color:var(--white);font-family:"Kumbh Sans",sans-serif;font-weight:700;font-size:52px;letter-spacing:-.5px}
.hero-sub{position:absolute;top:240px;left:190px;width:582px;text-align:center;color:var(--white);font-family:"Kumbh Sans",sans-serif;font-weight:600;font-size:19px;line-height:27px}
.hero-cta{position:absolute;top:315px;left:347px;width:268px;height:41px;background:var(--sky);color:var(--white);font-family:"Kumbh Sans",sans-serif;font-weight:600;font-size:17px;display:flex;align-items:center;justify-content:center;border-radius:2px;box-shadow:0 3px 0 #1e7fae}
.tools{position:absolute;top:526px;left:48px;width:866px;display:flex;gap:10px;align-items:flex-start}
.col{width:209px;display:flex;flex-direction:column;gap:10px}
.card{background:var(--card);padding:14px 14px 16px 14px}
.card.featured{border:3px solid var(--ice);padding:11px 11px 13px 11px}
.card-head{display:flex;align-items:center;gap:12px;margin-bottom:14px}
.icon{width:42px;height:42px;border-radius:50%;background:var(--ice);display:flex;align-items:center;justify-content:center;flex:none}
.card h2{font-family:"Kumbh Sans",sans-serif;font-weight:700;font-size:15.5px;color:var(--navy)}
.card p{font-size:11.3px;font-weight:300;line-height:19.2px;color:#333;margin-bottom:12px;padding-left:1px}
.more{display:inline-flex;align-items:center;height:32px;padding:0 8px;background:var(--sky);color:var(--white);font-family:"Kumbh Sans",sans-serif;font-weight:700;font-size:11.5px;border-radius:2px;box-shadow:0 2px 0 #1e7fae}
.footer{position:absolute;left:0;top:1125px;width:962px;height:75px;background:var(--navy);display:flex;align-items:center;padding:0 46px}
.copy{font-size:9px;color:var(--sky)}
.social{margin-left:auto;display:flex;gap:14px}
.social span{width:16px;height:16px;border-radius:50%;background:var(--white)}
</style>
</head>
<body>
<header class="hero">
  <div class="hero-photo" role="img" aria-label="Photo of a wooden desk with record turntables, headphones, a cassette and an open notebook with a pen"></div>
  <div class="hero-shade"></div>
  <div class="topbar">
    <div class="brand"><span class="brand-dot"></span>Lectern Hop</div>
    <nav class="nav">
      <a class="active">Home</a><a>My Classes</a><a>Tools</a><a>Contact</a><a>Lectern Hop</a>
    </nav>
    <div class="auth"><span class="btn-ghost">Sign In</span><span class="btn-solid">Sign Up</span></div>
  </div>
  <h1 class="hero-title">Welcome to Lectern Hop</h1>
  <p class="hero-sub">A collection of some fun and easy-to-use tools for building a classroom community and enabling active learning.</p>
  <div class="hero-cta">Sign up for An Account</div>
</header>

<main class="tools">
  <div class="col">
    <article class="card" style="height:258px">
      <div class="card-head"><span class="icon"><svg width="24" height="22" viewBox="0 0 24 22"><path d="M3 13V11a9 9 0 0 1 18 0v2" fill="none" stroke="#0355a3" stroke-width="2.4"/><rect x="1" y="12" width="6" height="9" rx="2" fill="#0355a3"/><rect x="17" y="12" width="6" height="9" rx="2" fill="#0355a3"/></svg></span><h2>Shuffle Pick</h2></div>
      <p>Where it all started! Students create playlists of upbeat music with TubeCast. At the start of class, one lucky student gets to be the class DJ. Typically paired with a “fib or fact” or “two truths and a lie” clicker activity.</p>
      <span class="more">Learn More&nbsp;›</span>
    </article>
    <article class="card" style="height:256px">
      <div class="card-head"><span class="icon"><svg width="18" height="20" viewBox="0 0 18 20"><path d="M4 6h10l2 14H2z" fill="#0355a3"/><path d="M6 6V4a3 3 0 0 1 6 0v2" fill="none" stroke="#0355a3" stroke-width="1.8"/></svg></span><h2>Extra Tambourine</h2></div>
      <p>Sometimes the think-pair-share discussions get so feverish the only prescription is extra tambourine. In other words, when the class gets too noisy you can ring this virtual bell to get everyone’s attention.</p>
      <span class="more">Learn More&nbsp;›</span>
    </article>
  </div>
  <div class="col">
    <article class="card featured" style="height:278px">
      <div class="card-head"><span class="icon"><svg width="22" height="20" viewBox="0 0 22 20"><rect x="2" y="3" width="11" height="15" rx="1.5" transform="rotate(-15 7 10)" fill="#0355a3"/><rect x="8" y="3" width="11" height="15" rx="1.5" transform="rotate(10 13 10)" fill="#33a6d7" stroke="#0355a3" stroke-width="1.2"/></svg></span><h2>FlashCards</h2></div>
      <p>Get to know each other! With Flashcards you can “flip” through student (and instructor) profiles, learn names, and a little bit about what makes them tick. A great first step for creating an interactive classroom community.</p>
      <span class="more">Learn More&nbsp;›</span>
    </article>
    <article class="card" style="height:266px">
      <div class="card-head"><span class="icon"><svg width="22" height="22" viewBox="0 0 22 22"><circle cx="11" cy="7" r="5" fill="#0355a3"/><path d="M2 21a9 7 0 0 1 18 0z" fill="#0355a3"/></svg></span><h2>Student Profiles</h2></div>
      <p>Instructor-customizable profiles let students share information about themselves with the class. Use it to find out what students expect to learn, their previous course- work, or just to help people get to know each other (see flashcards).</p>
      <span class="more">Learn More&nbsp;›</span>
    </article>
  </div>
  <div class="col">
    <article class="card" style="height:258px">
      <div class="card-head"><span class="icon"><svg width="20" height="24" viewBox="0 0 20 24"><path d="M10 1v7M6 8h8v5H6zM7 13l-4 5 2 5M13 13l4 5-2 5M10 13v8" fill="none" stroke="#0355a3" stroke-width="1.6"/></svg></span><h2>"The Grabber"</h2></div>
      <p>The grabber chooses who will go and who will stay...well it randomly chooses a student from the class roster anyway. It’s a fun way to encourage participation among quieter students and motivate active learning exercises.</p>
      <span class="more">Learn More&nbsp;›</span>
    </article>
    <article class="card" style="height:269px">
      <div class="card-head"><span class="icon"><svg width="22" height="20" viewBox="0 0 22 20"><rect x="2" y="3" width="15" height="15" rx="2" fill="none" stroke="#0355a3" stroke-width="2.2"/><path d="M6 10l4 4 10-12" fill="none" stroke="#0355a3" stroke-width="2.8"/></svg></span><h2>Self/Peer Evals</h2></div>
      <p>(coming Spring 2016) Self/Peer evaluations are a fantastic way to help students master material and deliver high quality feedback - fast. Works great in both large and small classes for either regular assignments or exams.</p>
      <span class="more">Learn More&nbsp;›</span>
    </article>
  </div>
  <div class="col">
    <article class="card" style="height:280px">
      <div class="card-head"><span class="icon"><svg width="16" height="24" viewBox="0 0 16 24"><rect x="1" y="1" width="14" height="22" rx="1" fill="#0355a3"/><rect x="9" y="4" width="3" height="16" fill="#cee9f5"/></svg></span><h2>Virtual Clicker</h2></div>
      <p>(coming soon) A simple tool for in-class polling. Launch multiple-choice questions from lecternhop.com or slides. Students respond via their laptop or smart phone. Bar graphs of the results (with “grabber” capabilities) link to student profiles.</p>
      <span class="more">Learn More&nbsp;›</span>
    </article>
    <article class="card" style="height:283px">
      <div class="card-head"><span class="icon"><svg width="22" height="22" viewBox="0 0 22 22"><path d="M11 2l9 4v10l-9 4-9-4V6z" fill="#0355a3"/><path d="M2 6l9 4 9-4M11 10v10" fill="none" stroke="#cee9f5" stroke-width="1"/></svg></span><h2>Rubrics</h2></div>
      <p>(coming Spring 2016) Rubrics are a great tool - both for providing guidance and feedback. This tool lets you create your own rubrics to use for assignments (self/peer evals for example). Also, you can search a database of existing rubrics to use as a starting point.</p>
      <span class="more">Learn More&nbsp;›</span>
    </article>
  </div>
</main>

<footer class="footer">
  <span class="copy">Copyright © 2016. Lectern Hop. All Right Reserved</span>
  <div class="social" aria-label="Social links"><span></span><span></span><span></span><span></span><span></span></div>
</footer>
</body>
</html>
```